CalmPeak Nurses' Manifesto

Design a manifesto to inspire and motivate nurses to work at minimum standards of excellence in their nursing practice.

The manifesto will become a feature of our website, at conferences, workshops and retreats. It will also be featured on other marketing tools.

Primary Market:
Nurses and/or other healthcare professionals (specifically Doctors, Occupational Therapists, Psychologists and Social Workers).

However the manifesto is equally applicable to all nurses and healthcare professionals from new graduates to very experienced senior clinicians, administration officers,managers and healthcare executive personnel.

Mainly females and primarily 35 to 65 years old, which suggests people in this target age group have extensive experience, but have become jaded'.

The purpose of our business is to assist healthcare professionals, primarily nurses, to maintain their enthusiasm and excellence in service provision, for their benefit as well as the benefit of the clients.

I have attached:
File 1: Copy Samples and examples: which has the copy for the manifesto, examples that appeal to us and our 3 attempts.
File 2: Our colour Spec Sheet, HOWEVER the colours are not necessary limited to these colours. These colours are not in the logo that will be on the manifesto. The colours on the logo attached can/or also be used.
File 3: Prototype logo. The final logo will be available within 3 to 4 days.

Industry/Entity Type

Healthcare

Requirements
Must have
• Must use the copy as per the attached file.

It should be contemporary, eye catching and motivational.

Should not have
• MUST BE EASY TO READ. Each line MUST be clearly defined from each other.

```html
<!DOCTYPE html>
<html lang="en">
<head>
<meta charset="utf-8">
<title>CalmPeak Nurses' Manifesto</title>
<link rel="stylesheet" href="https://fonts.googleapis.com/css2?family=Nunito:ital,wght@0,600;0,700;0,800;1,900&family=Oswald:wght@500&display=swap">
<style>
  :root {
    --teal: #1f9c98;
    --deep-teal: #245f66;
    --lime: #98c23c;
    --green: #33a86c;
    --mid-green: #2f9b78;
    --star: #a9adb1;
    --paper: #ffffff;
  }
  * { margin: 0; padding: 0; box-sizing: border-box; }
  html, body { width: 849px; height: 1200px; overflow: hidden; background: var(--paper); }
  .manifesto {
    position: relative;
    width: 849px;
    height: 1200px;
    overflow: hidden;
    background: var(--paper);
    font-family: "Nunito", "Arial Rounded MT Bold", sans-serif;
    font-weight: 700;
  }
  .line { position: absolute; white-space: nowrap; line-height: 1; }
  .condensed { font-family: "Oswald", "Arial Narrow", sans-serif; font-weight: 500; }
  .squeeze { transform-origin: 0 0; }
  .upright { transform-origin: 0 0; }

  .teal { color: var(--teal); }
  .deep { color: var(--deep-teal); }
  .lime { color: var(--lime); }
  .green { color: var(--green); }
  .mid { color: var(--mid-green); }

  .title { left: 10px; top: 4px; font-size: 38px; letter-spacing: 3.4px; }
  .self-care { left: 7px; top: 52px; font-size: 15px; line-height: 17.7px; }
  .deliver { left: 312px; top: 44px; font-size: 86px; transform: scaleX(0.66); }
  .respect { left: 9px; top: 140px; font-size: 58px; }
  .respect-copy { left: 199px; top: 144px; font-size: 25px; line-height: 33px; }
  .generously { left: 597px; top: 140px; font-size: 58px; transform: scaleX(0.84); }
  .support { left: 6px; top: 213px; font-size: 19px; letter-spacing: 1.1px; }
  .learn { left: 552px; top: 213px; font-size: 19px; letter-spacing: 0.5px; }
  .trust { left: 6px; top: 240px; font-size: 25px; letter-spacing: 0.9px; }
  .be-a-l { left: 7px; top: 260px; font-size: 92px; font-weight: 800; letter-spacing: -3px; }
  .lifelong { left: 283px; top: 279px; font-size: 28px; line-height: 34px; }
  .diversity { left: 414px; top: 279px; font-size: 29px; line-height: 35px; letter-spacing: 0.8px; }
  .distress { left: 6px; top: 347px; font-size: 34px; letter-spacing: 1px; }
  .smile { left: 6px; top: 389px; font-size: 34px; letter-spacing: 3.2px; }
  .have-fun { left: 232px; top: 432px; font-size: 70px; font-weight: 900; font-style: italic; letter-spacing: 1px; }
  .star { position: absolute; fill: var(--star); }
  .right-thing { left: 6px; top: 522px; font-size: 35px; letter-spacing: 2.6px; }
  .unique { left: 6px; top: 570px; font-size: 35px; letter-spacing: 3.1px; }
  .keep-going { left: 6px; top: 615px; font-size: 33px; letter-spacing: 2.5px; }
  .solution { left: 6px; top: 656px; font-size: 44px; letter-spacing: 2.6px; }
  .within { left: 6px; top: 716px; font-size: 41px; letter-spacing: 0.9px; }
  .follow { left: 6px; top: 769px; font-size: 41px; letter-spacing: 0.8px; }
  .be-who { left: 8px; top: 820px; font-size: 28.5px; line-height: 46px; }

  .only-follow { left: 650px; top: 895px; font-size: 46px; transform: rotate(-90deg) scaleX(0.95); }
  .exceptional { left: 702px; top: 895px; font-size: 72px; transform: rotate(-90deg) scaleX(0.65); }
  .leaders { left: 776px; top: 895px; font-size: 66px; transform: rotate(-90deg); }
  .live-your { left: 2px; top: 1166px; font-size: 56px; transform: rotate(-90deg); }
  .dream { left: 52px; top: 1166px; font-size: 140px; transform: rotate(-90deg) scaleX(0.66); }

  .lead-block { position: absolute; left: 204px; top: 914px; width: 632px; }
  .lead-line { display: block; width: 632px; white-space: nowrap; line-height: 36px; text-align: justify; text-align-last: justify; }
  .lead-1 { font-size: 26px; letter-spacing: 1.5px; }
  .lead-2 { font-size: 24px; letter-spacing: 0.8px; }
  .lead-3 { font-size: 24px; letter-spacing: 0.4px; }
  .lead-4 { font-size: 26px; letter-spacing: 1.4px; }
  .lead-5 { font-size: 22px; letter-spacing: 0.2px; }
  .lead-6 { font-size: 24px; letter-spacing: 0.6px; }

  .maker { position: absolute; left: 256px; top: 1142px; display: flex; align-items: center; gap: 10px; }
  .maker-square { width: 34px; height: 34px; background: var(--teal); }
  .maker-name { font-size: 20px; font-weight: 600; color: var(--deep-teal); }
</style>
</head>
<body>
<main class="manifesto" aria-label="CalmPeak Nurses' Manifesto">
  <h1 class="line title deep">Nurse with open hands, hearts &amp; minds</h1>
  <p class="line self-care lime">Look after yourself and value your health<br>as much as you value the health of others<br>Delight your clients and colleagues<br>by exceeding their expectations</p>
  <p class="line deliver condensed squeeze teal">DELIVER CARE SKIFULLY</p>

  <p class="line respect condensed lime">RESPECT</p>
  <p class="line respect-copy deep">the limits of people’s knowledge<br>andshare your knowledge</p>
  <p class="line generously condensed squeeze lime">GENEROUSLY</p>

  <p class="line support green">Support your colleagues and champion their purpose</p>
  <svg class="star" style="left:526px;top:211px" width="24" height="23" viewBox="0 0 100 95" aria-hidden="true"><polygon points="50,0 61,35 98,35 68,57 79,92 50,71 21,92 32,57 2,35 39,35"/></svg>
  <p class="line learn green">Learn something new each day</p>
  <p class="line trust mid">Trust your knowledge and seek advice only from respected sources</p>

  <p class="line be-a-l teal">BE A L</p>
  <p class="line lifelong teal">ifelong<br>earner</p>
  <p class="line diversity deep">Celebrate, respect and value<br>the diversity of your culture</p>

  <p class="line distress lime">Respond to distress with random acts of kindness</p>
  <p class="line smile lime">Smile and infect others with your happiness</p>

  <svg class="star" style="left:64px;top:434px" width="92" height="87" viewBox="0 0 100 95" aria-hidden="true"><polygon points="50,0 61,35 98,35 68,57 79,92 50,71 21,92 32,57 2,35 39,35"/></svg>
  <p class="line have-fun mid">Have fun!</p>
  <svg class="star" style="left:672px;top:434px" width="92" height="87" viewBox="0 0 100 95" aria-hidden="true"><polygon points="50,0 61,35 98,35 68,57 79,92 50,71 21,92 32,57 2,35 39,35"/></svg>

  <p class="line right-thing teal">Always do the right thing without exception</p>
  <p class="line unique deep">You are UNIQUE, revel in your individuality</p>
  <p class="line keep-going lime">Don’t ever believe you’ve arrived, KEEP GOING</p>
  <p class="line solution mid">Always be solution focused</p>
  <p class="line within green">Seek success firstly from within</p>
  <p class="line follow mid">Only follow exceptional leaders</p>
  <p class="line be-who lime">Be who you need to be and do whatyou need<br>to do to have the career you want to have</p>

  <p class="line upright only-follow green">Only follow</p>
  <p class="line upright exceptional condensed mid">EXCEPTIONAL</p>
  <p class="line upright leaders teal">leaders</p>

  <p class="line upright live-your lime">Live your</p>
  <p class="line upright dream condensed teal">DREAM</p>

  <p class="lead-block deep">
    <span class="lead-line lead-1">If there’s no one left to follow, then lead!</span>
    <span class="lead-line lead-2">Always lead with purpose, passion and commitment</span>
    <span class="lead-line lead-3">Respond to complex situations innovatively, creatively</span>
    <span class="lead-line lead-4">and safely within the scope of your practice</span>
    <span class="lead-line lead-5">Adopt a ‘CAN DO’ attitude to anything that comes your way</span>
    <span class="lead-line lead-6">Choose your thoughts wisely, they create your reality</span>
  </p>

  <footer class="maker">
    <span class="maker-square" aria-hidden="true"></span>
    <span class="maker-name">Ward Bloom Studio</span>
  </footer>
</main>
</body>
</html>
```